Business Card Design Project

We're an orthopaedic office, and our colors are blue white and balck. Dealing with physicians and healthcare execs, I'd like this card to have a classy, yet overpowering wow factor.

Here are a couple of cards I like that are close to what I'm looking for:
http://www.pixelbazaro.com/design/392047
http://www.pixelbazaro.com/design/286390

Industry/Entity Type

Healthcare

```html
<!DOCTYPE html>
<html lang="en">
<head>
<meta charset="utf-8">
<title>Crestline Orthopaedic – Business Card</title>
<link rel="stylesheet" href="https://fonts.googleapis.com/css2?family=Source+Sans+3:wght@400;600&display=swap">
<style>
  :root {
    --card-blue: #283a96;
    --ink-white: #ffffff;
    --stage: #ececee;
    --shadow: rgba(0, 0, 0, 0.28);
  }
  * { margin: 0; padding: 0; box-sizing: border-box; }
  html, body { width: 1200px; height: 789px; overflow: hidden; }
  body {
    background: var(--stage);
    font-family: "Source Sans 3", "Myriad Pro", sans-serif;
    color: var(--ink-white);
    position: relative;
  }
  .card {
    position: absolute;
    width: 520px;
    height: 298px;
    background: var(--card-blue);
    box-shadow: 0 8px 22px var(--shadow);
  }
  .card--front { left: 60px; top: 150px; }
  .card--back  { left: 620px; top: 340px; }

  .brand {
    display: flex;
    align-items: center;
    gap: 12px;
  }
  .brand__dot {
    width: 46px;
    height: 46px;
    border-radius: 50%;
    background: var(--ink-white);
    flex: none;
  }
  .brand__name {
    font-weight: 400;
    line-height: 1.05;
  }
  .brand__title { display: block; font-size: 27px; letter-spacing: 0.5px; text-transform: uppercase; }
  .brand__tag { display: block; font-size: 12px; }

  .card--front .brand { position: absolute; left: 42px; top: 52px; }

  .card--back .brand {
    position: absolute;
    left: 50%;
    top: 50%;
    transform: translate(-50%, -50%);
  }

  .contact {
    position: absolute;
    left: 42px;
    bottom: 34px;
    font-size: 15px;
    line-height: 1.28;
  }
  .contact__name { font-size: 17px; margin-bottom: 2px; }
  .contact__role { margin-left: 22px; }
</style>
</head>
<body>
  <section class="card card--front" aria-label="Business card front">
    <div class="brand">
      <span class="brand__dot" aria-hidden="true"></span>
      <span class="brand__name">
        <span class="brand__title">Crestline</span>
        <span class="brand__tag">Orthopaedic &amp; Sports Medicine Center</span>
      </span>
    </div>
    <address class="contact">
      <p class="contact__name">Dalton Reese – <span class="contact__role">CEO</span></p>
      <p>(318) 555-0142</p>
      <p>dreese@crestlineortho.com</p>
      <p>1820 Harbor Ln., Fairview, LA 70412</p>
    </address>
  </section>

  <section class="card card--back" aria-label="Business card back">
    <div class="brand">
      <span class="brand__dot" aria-hidden="true"></span>
      <span class="brand__name">
        <span class="brand__title">Crestline</span>
        <span class="brand__tag">Orthopaedic &amp; Sports Medicine Center</span>
      </span>
    </div>
  </section>
</body>
</html>
```